Upscale business cards needed for Board of Directors

We need professional business cards created for members of our family business Board of Directors. We would like these relatively simple and straightforward, but also with a unique element to set them apart. Probably stick with neutral and simple colors - white, grey etc. We need space for the traditional elements, including name, title, address, email/phone number. And we will be creating several from this template so it needs to be template that is easy to switch information in and out of.
Business
See description

```html
<!DOCTYPE html>
<html lang="en">
<head>
<meta charset="utf-8">
<title>Harborline Holdings – Business Card</title>
<link href="https://fonts.googleapis.com/css2?family=Montserrat:wght@400;500;800&display=swap" rel="stylesheet">
<style>
  :root {
    --ink: #0d0d0d;
    --paper: #ffffff;
    --gold: #b9a57c;
    --text: #2a2a2a;
    --stage: #e9e8e6;
  }
  * { margin: 0; padding: 0; box-sizing: border-box; }
  html, body { width: 1200px; height: 1022px; overflow: hidden; }
  body {
    background: var(--stage);
    font-family: "Montserrat", Arial, sans-serif;
    color: var(--text);
    position: relative;
  }
  .card {
    position: absolute;
    left: 250px;
    width: 700px;
    height: 400px;
    border-radius: 18px;
    overflow: hidden;
    box-shadow: 0 6px 20px rgba(0,0,0,.12);
  }
  .card--front { top: 80px; }
  .card--back { top: 542px; }
  .card__shape { position: absolute; inset: 0; }
  .card__content { position: absolute; left: 44px; top: 46px; width: 420px; }
  .brand__rule { width: 250px; height: 6px; background: var(--gold); margin-bottom: 10px; }
  .brand__name {
    font-weight: 800; color: var(--ink); text-transform: uppercase; line-height: 1;
  }
  .brand__name--main { font-size: 44px; letter-spacing: -0.5px; }
  .brand__name--sub { font-size: 24px; letter-spacing: 12px; margin-top: 6px; }
  .person { margin-top: 26px; }
  .person__name { font-size: 30px; font-weight: 500; color: var(--gold); line-height: 1.1; }
  .person__title { font-size: 16px; margin-top: 4px; }
  .address { margin-top: 14px; font-size: 16px; line-height: 1.4; }
  .contact { list-style: none; margin-top: 10px; font-size: 16px; line-height: 1.45; }
  .contact__item { display: flex; align-items: center; gap: 10px; }
  .contact__icon { width: 14px; height: 14px; flex: none; }
  .contact__accent { color: var(--gold); }
</style>
</head>
<body>

<section class="card card--front">
  <svg class="card__shape" viewBox="0 0 700 400" aria-hidden="true">
    <rect width="700" height="400" fill="var(--ink)"/>
    <path d="M0 0 H320 A200 200 0 0 1 320 400 H0 Z" fill="var(--paper)"/>
    <path d="M320 -12 A212 212 0 0 1 320 412" fill="none" stroke="var(--gold)" stroke-width="5"/>
  </svg>
  <div class="card__content">
    <div class="brand">
      <div class="brand__rule"></div>
      <div class="brand__name brand__name--main">Harborline</div>
      <div class="brand__name brand__name--sub">Holdings</div>
    </div>
    <div class="person">
      <div class="person__name">Marcus Ellery</div>
      <div class="person__title">Director</div>
    </div>
    <div class="address">2815 Linden Ave.<br>Pasadena CA 91101</div>
    <ul class="contact">
      <li class="contact__item">
        <svg class="contact__icon" viewBox="0 0 16 16"><path d="M3 1h3l1.5 4-2 1.2a9 9 0 0 0 4.3 4.3L11 8.5l4 1.5v3a2 2 0 0 1-2 2A13 13 0 0 1 1 3a2 2 0 0 1 2-2z" fill="var(--gold)"/></svg>
        +330 5550-1234
      </li>
      <li class="contact__item">
        <svg class="contact__icon" viewBox="0 0 16 16"><rect x="1" y="3" width="14" height="10" fill="none" stroke="var(--gold)" stroke-width="1.6"/><path d="M1 3l7 6 7-6" fill="none" stroke="var(--gold)" stroke-width="1.6"/></svg>
        info@harborlineholdings.com
      </li>
      <li class="contact__item">
        <svg class="contact__icon" viewBox="0 0 16 16"><circle cx="8" cy="8" r="7" fill="none" stroke="var(--gold)" stroke-width="1.6"/><path d="M1 8h14M8 1c-3 3.5-3 10.5 0 14M8 1c3 3.5 3 10.5 0 14" fill="none" stroke="var(--gold)" stroke-width="1.2"/></svg>
        www.<span class="contact__accent">harborlineholdings</span>.com
      </li>
    </ul>
  </div>
</section>

<section class="card card--back">
  <svg class="card__shape" viewBox="0 0 700 400" aria-hidden="true">
    <rect width="700" height="400" fill="var(--ink)"/>
    <path d="M0 0 H380 A200 200 0 0 1 380 400 H0 Z" fill="var(--ink)"/>
    <path d="M210 0 H380 A200 200 0 0 1 380 400 H210 A200 200 0 0 1 210 0 Z" fill="var(--paper)"/>
    <path d="M210 -12 H380 A212 212 0 0 1 380 412 H210 A212 212 0 0 1 210 -12 Z" fill="none" stroke="var(--gold)" stroke-width="5"/>
  </svg>
</section>

</body>
</html>
```